Harbor Allied BC

I have a baseline business card that I would like to spruce up!

I actually like this business card. I just want to find a way to have all the information below on it and it too look balanced and professional.

Target Market(s)

Small to medium sized companies - Health Insurance Consulting

Industry/Entity Type

Health Insurance

Contact Information for Business Card

The information I would like included on the business card is:

- Harbor Allied Southridge Title and logo
- Tessa Wrenfield
- Business title: Principal
- 4192 Cobalt Ridge Rd Suite D-117 Larkhaven, WA 98999
- Employee Benefits Consulting & (Wellness Consulting) optional
- tessa@harboralliedsr.example
- cell: 425-555-0183

Font styles to use
Other font styles liked:
• I like the font it is currently in but am open to others.

Requirements
Must have
• I like the logo and the color scheme. I even like the layout. I just need to fine tune it!

```html
<!DOCTYPE html>
<html lang="en">
<head>
<meta charset="utf-8">
<title>Harbor Allied Southridge – Business Card</title>
<link href="https://fonts.googleapis.com/css2?family=Arimo:wght@400;700&display=swap" rel="stylesheet">
<style>
  :root {
    --backdrop: #1f1f1f;
    --brand-green: #0b8a55;
    --brand-green-dark: #077a4a;
    --card-white: #fbfbfb;
    --ink: #2a2a2a;
    --divider: #9a9a9a;
  }
  * { box-sizing: border-box; margin: 0; padding: 0; }
  html, body {
    width: 1200px; height: 873px; overflow: hidden;
    background: var(--backdrop);
    font-family: "Arimo", Arial, sans-serif;
  }
  .canvas {
    position: relative; width: 1200px; height: 873px;
    display: flex; align-items: center; justify-content: center; gap: 40px;
  }
  .card {
    position: relative; width: 530px; height: 303px;
    border-radius: 22px; overflow: hidden;
  }
  /* Front */
  .card--front {
    background: linear-gradient(160deg, #0d9a5f 0%, var(--brand-green) 55%, var(--brand-green-dark) 100%);
    display: flex; align-items: center; justify-content: center; gap: 16px;
  }
  .brand-dot { flex: none; border-radius: 50%; }
  .card--front .brand-dot { width: 58px; height: 58px; background: #ffffff; }
  .card--front .brand-name {
    color: #ffffff; font-weight: 400; font-size: 23px; letter-spacing: 0.5px;
    text-transform: uppercase;
  }
  /* Back */
  .card--back { background: var(--card-white); }
  .brand-row {
    position: absolute; left: 36px; top: 46px;
    display: flex; align-items: center; gap: 12px;
  }
  .card--back .brand-dot { width: 44px; height: 44px; background: var(--brand-green); }
  .card--back .brand-name {
    color: var(--ink); font-weight: 400; font-size: 17px; letter-spacing: 0.3px;
    text-transform: uppercase;
  }
  .brand-divider { width: 1px; height: 52px; background: var(--divider); margin-left: 6px; }
  .tagline {
    color: var(--brand-green); font-size: 12px; line-height: 14px; letter-spacing: 0.6px;
  }
  .person { position: absolute; left: 36px; top: 134px; }
  .person__name {
    color: var(--brand-green); font-weight: 700; font-size: 18px; letter-spacing: 0.8px;
  }
  .person__role {
    color: var(--ink); font-weight: 700; font-size: 13px; letter-spacing: 0.6px; margin-top: 4px;
  }
  .rule {
    position: absolute; left: 116px; right: 30px; top: 167px;
    height: 1.5px; background: var(--brand-green);
  }
  .address {
    position: absolute; right: 30px; top: 182px; text-align: right;
    font-style: normal;
    color: var(--ink); font-size: 13px; line-height: 17px; letter-spacing: 0.8px;
  }
  .contacts { position: absolute; left: 36px; top: 228px; list-style: none; }
  .contacts li {
    display: flex; align-items: center; gap: 9px;
    color: var(--ink); font-size: 14px; letter-spacing: 0.8px; margin-bottom: 9px;
  }
  .contacts svg { width: 16px; height: 16px; flex: none; }
</style>
</head>
<body>
<main class="canvas">
  <section class="card card--front" aria-label="Card front">
    <span class="brand-dot"></span>
    <span class="brand-name">Harbor Allied Southridge</span>
  </section>

  <section class="card card--back" aria-label="Card back">
    <div class="brand-row">
      <span class="brand-dot"></span>
      <span class="brand-name">Harbor Allied Southridge</span>
      <span class="brand-divider"></span>
      <p class="tagline">Employee<br>Benefits<br>Consulting</p>
    </div>

    <div class="person">
      <p class="person__name">Tessa Wrenfield</p>
      <p class="person__role">Principal</p>
    </div>
    <div class="rule"></div>

    <address class="address">
      4192 Cobalt Ridge Rd Suite<br>D-117 Larkhaven,<br>WA 98999
    </address>

    <ul class="contacts">
      <li>
        <svg viewBox="0 0 16 16" aria-hidden="true">
          <rect width="16" height="16" rx="4" fill="#0b8a55"/>
          <rect x="5" y="3" width="6" height="10" rx="1.2" fill="none" stroke="#fff" stroke-width="1.3"/>
          <circle cx="8" cy="11.2" r="0.7" fill="#fff"/>
        </svg>
        425-555-0183
      </li>
      <li>
        <svg viewBox="0 0 16 16" aria-hidden="true">
          <rect width="16" height="16" rx="4" fill="#0b8a55"/>
          <rect x="3.5" y="5" width="9" height="6.5" rx="0.8" fill="none" stroke="#fff" stroke-width="1.2"/>
          <path d="M3.8 5.4 L8 8.6 L12.2 5.4" fill="none" stroke="#fff" stroke-width="1.2"/>
        </svg>
        tessa@harboralliedsr.example
      </li>
    </ul>
  </section>
</main>
</body>
</html>
```